Business Card Design Project

We need a business card design for a new construction company called 'KORVA HOLDINGS PTY.LTD' We run a construction based company for high end market homes in melbourne, we want something that looks professional and eye catching.The card needs to have a strong design to it something modern as the company name explains "korva." The final design should communicate professionalism and a strong image to our customers on the quality of our work.
On the business card i need
Name: Marek Holtvay
Mob:0417295031
Email:korva.holdings@mailbrook.example
Domestic/Residential/Commercial

```html
<!DOCTYPE html>
<html lang="en">
<head>
<meta charset="utf-8">
<title>Korva Holdings – Business Card</title>
<link rel="stylesheet" href="https://fonts.googleapis.com/css2?family=Source+Sans+3:wght@400;600;700&display=swap">
<style>
  :root {
    --backdrop: #e6e4e1;
    --card-light: #ffffff;
    --card-dark: #2a2828;
    --ink: #2b2a2a;
    --ink-soft: #3a3a3a;
    --accent: #e3232b;
    --on-dark: #ffffff;
  }
  * { margin: 0; padding: 0; box-sizing: border-box; }
  html, body {
    width: 1200px; height: 900px; overflow: hidden;
    background: var(--backdrop);
    font-family: "Source Sans 3", Arial, sans-serif;
  }
  .canvas { position: relative; width: 1200px; height: 900px; }
  .card {
    position: absolute; top: 245px; width: 556px; height: 356px;
    overflow: hidden; box-shadow: 0 4px 14px rgba(0,0,0,0.18);
  }
  .card--front { left: 33px; background: var(--card-light); }
  .card--back { left: 618px; background: var(--card-dark); }

  .brand { position: absolute; }
  .brand__name {
    display: block; font-weight: 700; font-size: 62px; line-height: 1;
    letter-spacing: 1px; text-transform: uppercase;
  }
  .brand__legal {
    display: block; color: var(--accent); font-weight: 600;
    font-size: 10px; letter-spacing: 3.2px; margin-top: 4px;
  }
  .card--front .brand { left: 27px; top: 30px; }
  .card--front .brand__name { color: var(--ink); }
  .card--back .brand { left: 0; right: 0; top: 130px; text-align: center; }
  .card--back .brand__name { color: var(--on-dark); }
  .card--back .brand__legal { padding-left: 90px; }

  .services { position: absolute; font-size: 15px; white-space: nowrap; }
  .services__sep { color: var(--accent); padding: 0 2px; }
  .card--front .services { left: 276px; top: 68px; color: var(--ink-soft); }
  .card--back .services {
    left: 0; right: 0; top: 228px; text-align: center;
    color: var(--on-dark); font-size: 19px;
  }

  .person { position: absolute; left: 7px; top: 240px; }
  .person__name { color: var(--accent); font-weight: 700; font-size: 25px; margin-bottom: 14px; }
  .contact { font-size: 14px; color: var(--ink); line-height: 1.45; list-style: none; }
  .contact__label { color: var(--accent); font-weight: 700; }

  .card__base {
    position: absolute; left: 0; bottom: 0; width: 100%; height: 12px;
    background: var(--ink);
  }
  .card__mark {
    position: absolute; right: 22px; bottom: 12px; width: 64px; height: 64px;
    background: var(--ink);
  }
</style>
</head>
<body>
<main class="canvas">
  <section class="card card--front">
    <div class="brand">
      <span class="brand__name">korva</span>
      <span class="brand__legal">KORVA HOLDINGS PTY.LTD</span>
    </div>
    <p class="services">Domestic <span class="services__sep">|</span>Residential <span class="services__sep">|</span>Commercial</p>
    <div class="person">
      <h1 class="person__name">Marek Holtvay</h1>
      <ul class="contact">
        <li><span class="contact__label">Mobile</span> : 0417295031</li>
        <li><span class="contact__label">Email</span> : korva.holdings@mailbrook.example</li>
      </ul>
    </div>
    <div class="card__mark"></div>
    <div class="card__base"></div>
  </section>

  <section class="card card--back">
    <div class="brand">
      <span class="brand__name">korva</span>
      <span class="brand__legal">KORVA HOLDINGS PTY.LTD</span>
    </div>
    <p class="services">Domestic <span class="services__sep">|</span>Residential <span class="services__sep">|</span>Commercial</p>
  </section>
</main>
</body>
</html>
```